PawHush business card

Looking for a fun and cool biz card for a new company with patent pending products. I have products to help and protect dogs hearing. My colors are pantone blue and orange.
Updates

Please add tag line: Protect the ones you love...even your PawHushes!

Target Market(s)

Animal/Dog lovers!

Industry/Entity Type

Retail

Contact Information for Business Card

I'm looking for something simple yet fun with all the info included for biz cards

Colors
0555a3
f78f20

Requirements
Must have
• Logo
Nice to have
• name, website and email
Should not have
• phone number

```html
<!DOCTYPE html>
<html lang="en">
<head>
<meta charset="utf-8">
<title>PawHush business card</title>
<link rel="stylesheet" href="https://fonts.googleapis.com/css2?family=Montserrat:wght@500;600;700;800&display=swap">
<style>
  :root {
    --navy: #2a3d85;
    --orange: #f05a22;
    --paper: #efeeec;
    --white: #ffffff;
    --backdrop: #e4e4e6;
  }
  * { margin: 0; padding: 0; box-sizing: border-box; }
  html, body {
    width: 1200px;
    height: 1000px;
    overflow: hidden;
    background: var(--backdrop);
    font-family: "Montserrat", sans-serif;
  }
  .canvas {
    position: relative;
    width: 1200px;
    height: 1000px;
  }
  .card {
    position: absolute;
    width: 600px;
    height: 360px;
    border-radius: 34px;
    padding: 28px;
    box-shadow: 0 10px 26px rgba(0, 0, 0, 0.18);
  }
  .card-inner {
    width: 100%;
    height: 100%;
    border-radius: 22px;
    display: flex;
    flex-direction: column;
    align-items: center;
    justify-content: center;
  }

  /* Front: navy face with white frame */
  .card-front {
    left: 90px;
    top: 90px;
    background: var(--white);
  }
  .card-front .card-inner { background: var(--navy); }

  /* Back: paper face with navy frame */
  .card-back {
    left: 510px;
    top: 540px;
    background: var(--navy);
  }
  .card-back .card-inner { background: var(--paper); }

  .brand {
    display: flex;
    align-items: center;
    gap: 14px;
    color: var(--orange);
    font-weight: 700;
    letter-spacing: -0.5px;
    line-height: 1;
  }
  .brand-dot {
    border-radius: 50%;
    background: var(--orange);
  }
  .card-front .brand { font-size: 78px; }
  .card-front .brand-dot { width: 26px; height: 26px; }
  .card-back .brand { font-size: 66px; margin-bottom: 24px; }
  .card-back .brand-dot { width: 22px; height: 22px; }

  .holder-name {
    color: var(--orange);
    font-size: 26px;
    font-weight: 600;
    letter-spacing: 1px;
    margin-bottom: 18px;
  }
  .contact {
    list-style: none;
    text-align: center;
    font-size: 19px;
    font-weight: 500;
    line-height: 1.45;
  }
  .contact-label { color: var(--orange); }
  .contact-value { color: var(--navy); }
</style>
</head>
<body>
  <main class="canvas">
    <section class="card card-front" aria-label="Business card front">
      <div class="card-inner">
        <div class="brand"><span class="brand-dot"></span>PawHush</div>
      </div>
    </section>

    <section class="card card-back" aria-label="Business card back">
      <div class="card-inner">
        <div class="brand"><span class="brand-dot"></span>PawHush</div>
        <p class="holder-name">YOUR NAME</p>
        <ul class="contact">
          <li><span class="contact-label">E-mail : </span><span class="contact-value">info@pawhush.com</span></li>
          <li><span class="contact-label">Web : </span><span class="contact-value">www.pawhush.com</span></li>
        </ul>
      </div>
    </section>
  </main>
</body>
</html>
```